Harbor Growth Circle Powerpoint Template

We need a Powerpoint template to use for a professional association called the Harbor Growth Circle. The design should incorporate a logo that we will attach. We're looking for something clean, elegant, and professional. I'm attaching a sample Powerpoint file with 2 slides of content that we'd like to have designed so that they look good and incorporate the logo. The intention is that we can then take that template and create more content on our own.

Font styles to use
Sans Serif

```html
<!DOCTYPE html>
<html lang="en">
<head>
<meta charset="utf-8">
<title>Harbor Growth Circle – Presentation Template</title>
<link rel="stylesheet" href="https://fonts.googleapis.com/css2?family=Rubik:wght@400;500;600;700&display=swap">
<style>
:root{
  --navy:#0a3a8a;
  --deep:#072c6b;
  --blue:#0b5cc0;
  --sky:#1a75d1;
  --ink:#1f2630;
  --muted:#4b525c;
  --canvas:#e3e4e6;
  --white:#ffffff;
  --rule:#d7dbe2;
}
*{box-sizing:border-box;margin:0;padding:0}
html,body{width:1200px;height:4158px;overflow:hidden}
body{background:var(--canvas);font-family:"Rubik",Arial,sans-serif;color:var(--ink);position:relative}
.slide{position:absolute;width:559px;height:315px;overflow:hidden;background:var(--white)}
.c1{left:26px}.c2{left:614px}.cc{left:321px}
.r1{top:29px}.r2{top:373px}.r3{top:717px}.r4{top:1061px}.r5{top:1405px}.r6{top:1749px}
.r7{top:2093px}.r8{top:2437px}.r9{top:2781px}.r10{top:3125px}.r11{top:3469px}.r12{top:3815px}
.fill{position:absolute;inset:0}
.decor{position:absolute;inset:0;width:559px;height:315px}
.abs{position:absolute}

/* brand lockup */
.brand{position:absolute;left:45px;top:50px;width:104px;text-align:center;color:var(--white)}
.brand i{display:block;margin:0 auto;width:17px;height:17px;border:2.5px solid currentColor;border-radius:50%}
.brand span{display:block;margin-top:6px;font-size:5px;font-weight:600;letter-spacing:.05em;text-transform:uppercase;white-space:nowrap}
.light .brand{color:var(--navy)}
.light .brand span{color:var(--blue)}
.centered .brand{left:50%;margin-left:-52px}

/* cover type */
.cover .title{position:absolute;left:45px;top:124px;font-size:30px;line-height:1.1;font-weight:600;color:var(--white)}
.cover .sub{position:absolute;left:45px;top:210px;font-size:15px;line-height:1.05;font-weight:400;color:var(--white)}
.cover .date{position:absolute;left:45px;top:263px;font-size:7.5px;color:var(--white)}
.cover.light .title{color:var(--navy)}
.cover.light .sub{color:var(--sky)}
.cover.light .date{color:var(--ink)}
.cover.centered .title,.cover.centered .sub,.cover.centered .date{left:0;width:100%;text-align:center}
.cover.centered .sub{top:205px;font-size:14px}
.cover.centered .date{top:254px}
.shift .brand{left:184px}
.shift .title,.shift .sub,.shift .date{left:184px!important}

/* content chrome */
.mark{position:absolute;right:18px;top:22px;width:18px;height:18px;border:2.5px solid var(--blue);border-radius:50%}
.mark.on-blue{border-color:var(--white)}
.pg{position:absolute;right:12px;bottom:10px;width:8px;height:8px;background:var(--blue)}
.pg.on-blue{background:var(--white)}
.stitle{position:absolute;left:24px;top:18px;font-size:19px;font-weight:500;color:var(--navy);white-space:nowrap}
.stitle b{color:var(--blue);font-weight:600}
.stitle.plain{color:var(--ink);font-weight:400}
.stitle.plain b{color:var(--blue);font-weight:500}
.body{font-size:7px;line-height:1.3;color:var(--muted)}
.item-t{font-size:10px;line-height:1.1;color:var(--blue);font-weight:500}
.tiny{font-size:5.6px;line-height:1.3;color:var(--muted)}

/* table of contents */
.toc-row{position:absolute;display:flex;align-items:flex-start;gap:12px;width:175px}
.toc-row .num{font-size:20px;color:#a9b0bb;font-weight:400;line-height:1;width:14px;text-align:right}
.toc-row .item-t{margin-bottom:2px}

/* bullets */
ul.bul{list-style:none}
ul.bul li{position:relative;padding-left:9px;margin-bottom:3px}
ul.bul li::before{content:"";position:absolute;left:0;top:3px;width:3.5px;height:3.5px;border-radius:50%;background:var(--blue)}

/* icon circles */
.ico{position:absolute;width:28px;height:28px;border-radius:50%;background:var(--blue);display:flex;align-items:center;justify-content:center}
.ico svg{width:15px;height:15px}
.ico.white{background:var(--white)}

/* partner table */
.ptable{position:absolute;left:22px;top:68px;width:517px;border-collapse:collapse;table-layout:fixed}
.ptable th{background:var(--blue);color:var(--white);font-size:7.5px;font-weight:400;text-align:left;padding:5px 4px;border-right:1px solid var(--white)}
.ptable td{font-size:5px;line-height:1.25;color:var(--muted);padding:0 4px;height:29px;vertical-align:middle}
.ptable tr:nth-child(even) td{background:#f1f3f6}
.ptable td:first-child{color:var(--ink)}

/* data table */
.dtable{position:absolute;left:287px;top:116px;width:240px;border-collapse:collapse;table-layout:fixed}
.dtable th{background:var(--navy);color:var(--white);font-size:6.5px;font-weight:400;text-align:left;padding:4px 5px}
.dtable td{font-size:6px;color:var(--ink);padding:3px 5px;border-bottom:1px solid var(--rule);height:17px}
.dtable td+td,.dtable th+th{text-align:center}

.contact-line{position:absolute;left:47px;display:flex;align-items:center;gap:6px;font-size:7px;color:var(--white)}
.contact-line svg{width:8px;height:8px}
</style>
</head>
<body>

<!-- Row 1 -->
<section class="slide c1 r1 cover">
  <div class="fill" role="img" aria-label="Photo of glass office towers rising into a cloudy sky, tinted blue" style="background:linear-gradient(100deg,#0a3f98 0%,#0d4ea8 40%,#3d76bb 70%,#a9c0dc 100%)"></div>
  <svg class="decor" viewBox="0 0 559 315" aria-hidden="true">
    <polygon points="559,128 559,315 392,315" fill="#fff"/>
    <circle cx="545" cy="300" r="92" fill="#0b5cc0"/>
  </svg>
  <div class="brand"><i></i><span>Harbor Growth Circle</span></div>
  <h1 class="title">Presentation<br>Title Goes Here!</h1>
  <p class="sub">Subtitle of Presentation<br>Goes Here!</p>
  <p class="date">Saturday, April 17, 2021</p>
</section>

<section class="slide c2 r1 cover">
  <div class="fill" role="img" aria-label="Dark blue background of glowing connected network points" style="background:radial-gradient(circle at 70% 40%,#2a7ad6 0%,#0b4fae 45%,#07327a 100%)"></div>
  <svg class="decor" viewBox="0 0 559 315" aria-hidden="true">
    <polygon points="559,128 559,315 392,315" fill="#fff"/>
    <circle cx="545" cy="300" r="92" fill="#0b5cc0"/>
  </svg>
  <div class="brand"><i></i><span>Harbor Growth Circle</span></div>
  <h1 class="title">Presentation<br>Title Goes Here!</h1>
  <p class="sub">Subtitle of Presentation<br>Goes Here!</p>
  <p class="date">Saturday, April 17, 2021</p>
</section>

<!-- Row 2 -->
<section class="slide c1 r2 cover" style="background:var(--blue)">
  <svg class="decor" viewBox="0 0 559 315" aria-hidden="true">
    <polygon points="548,0 559,0 559,315 380,315" fill="#fff"/>
    <polygon points="559,70 559,315 430,315" fill="#0a3a8a"/>
    <circle cx="548" cy="300" r="80" fill="#1a75d1"/>
  </svg>
  <div class="brand"><i></i><span>Harbor Growth Circle</span></div>
  <h1 class="title">Presentation<br>Title Goes Here!</h1>
  <p class="sub">Subtitle of Presentation<br>Goes Here!</p>
  <p class="date">Saturday, April 17, 2021</p>
</section>

<section class="slide c2 r2 cover light">
  <svg class="decor" viewBox="0 0 559 315" aria-hidden="true">
    <polygon points="555,0 559,0 559,315 370,315" fill="#0b5cc0"/>
    <polygon points="559,80 559,315 425,315" fill="#0a3a8a"/>
    <circle cx="548" cy="300" r="78" fill="#fff"/>
  </svg>
  <div class="brand"><i></i><span>Harbor Growth Circle</span></div>
  <h1 class="title">Presentation<br>Title Goes Here!</h1>
  <p class="sub">Subtitle of Presentation<br>Goes Here!</p>
  <p class="date">Saturday, April 17, 2021</p>
</section>

<!-- Row 3 -->
<section class="slide c1 r3 cover light">
  <svg class="decor" viewBox="0 0 559 315" aria-hidden="true">
    <circle cx="540" cy="157" r="84" fill="#0b5cc0"/>
  </svg>
  <div class="brand"><i></i><span>Harbor Growth Circle</span></div>
  <h1 class="title">Presentation<br>Title Goes Here!</h1>
  <p class="sub">Subtitle of Presentation<br>Goes Here!</p>
  <p class="date">Saturday, April 17, 2021</p>
</section>

<section class="slide c2 r3 cover light shift">
  <svg class="decor" viewBox="0 0 559 315" aria-hidden="true">
    <circle cx="22" cy="157" r="84" fill="#0b5cc0"/>
  </svg>
  <div class="brand"><i></i><span>Harbor Growth Circle</span></div>
  <h1 class="title">Presentation<br>Title Goes Here!</h1>
  <p class="sub">Subtitle of Presentation<br>Goes Here!</p>
  <p class="date">Saturday, April 17, 2021</p>
</section>

<!-- Row 4 -->
<section class="slide c1 r4 cover light">
  <svg class="decor" viewBox="0 0 559 315" aria-hidden="true">
    <polygon points="410,0 559,0 559,250" fill="#0a3a8a"/>
    <polygon points="440,0 559,0 559,205" fill="#0b5cc0"/>
    <circle cx="540" cy="25" r="70" fill="#1a75d1"/>
  </svg>
  <div class="brand"><i></i><span>Harbor Growth Circle</span></div>
  <h1 class="title">Presentation<br>Title Goes Here!</h1>
  <p class="sub">Subtitle of Presentation<br>Goes Here!</p>
  <p class="date">Saturday, April 17, 2021</p>
</section>

<section class="slide c2 r4 cover centered">
  <div class="fill" role="img" aria-label="Deep blue background of glowing connected network lines over a globe" style="background:radial-gradient(ellipse at 50% 90%,#2e86e0 0%,#0c55b4 45%,#073073 100%)"></div>
  <div class="brand" style="top:40px"><i></i><span>Harbor Growth Circle</span></div>
  <h1 class="title" style="top:122px">Harbor<br>Growth Circle</h1>
  <p class="sub">Subtitle of Presentation Goes Here!</p>
  <p class="date">Saturday, April 17, 2021</p>
</section>

<!-- Row 5 -->
<section class="slide c1 r5 cover centered">
  <div class="fill" role="img" aria-label="Photo looking up at glass office towers under a cloudy sky, tinted blue" style="background:linear-gradient(180deg,#6d8fbd 0%,#1e5aa6 40%,#0b3f90 100%)"></div>
  <div class="brand" style="top:40px"><i></i><span>Harbor Growth Circle</span></div>
  <h1 class="title" style="top:122px">Harbor<br>Growth Circle</h1>
  <p class="sub">Subtitle of Presentation Goes Here!</p>
  <p class="date">Saturday, April 17, 2021</p>
</section>

<section class="slide c2 r5">
  <svg class="decor" viewBox="0 0 559 315" aria-hidden="true">
    <circle cx="30" cy="315" r="112" fill="#0b5cc0"/>
  </svg>
  <h2 class="stitle plain" style="left:24px;top:20px">Table of <b>Contents</b></h2>
  <div class="mark"></div>
  <div class="toc-row" style="left:122px;top:90px"><span class="num">1</span><div><p class="item-t">Title Goes Here!</p><p class="tiny">Lorem ipsum dolor sit amet, at laborum nibh duis mauris. Per ultrices lectus sed</p></div></div>
  <div class="toc-row" style="left:122px;top:140px"><span class="num">2</span><div><p class="item-t">Title Goes Here!</p><p class="tiny">Lorem ipsum dolor sit amet, at laborum nibh duis mauris. Per ultrices lectus sed</p></div></div>
  <div class="toc-row" style="left:328px;top:90px"><span class="num">3</span><div><p class="item-t">Title Goes Here!</p><p class="tiny">Lorem ipsum dolor sit amet, at laborum nibh duis mauris. Per ultrices lectus sed</p></div></div>
  <div class="toc-row" style="left:328px;top:140px"><span class="num">4</span><div><p class="item-t">Title Goes Here!</p><p class="tiny">Lorem ipsum dolor sit amet, at laborum nibh duis mauris. Per ultrices lectus sed</p></div></div>
  <div class="toc-row" style="left:328px;top:190px"><span class="num">5</span><div><p class="item-t">Title Goes Here!</p><p class="tiny">Lorem ipsum dolor sit amet, at laborum nibh duis mauris. Per ultrices lectus sed</p></div></div>
  <div class="toc-row" style="left:328px;top:240px"><span class="num">6</span><div><p class="item-t">Title Goes Here!</p><p class="tiny">Lorem ipsum dolor sit amet, at laborum nibh duis mauris. Per ultrices lectus sed</p></div></div>
  <div class="pg"></div>
</section>

<!-- Row 6 -->
<section class="slide c1 r6">
  <div class="abs" role="img" aria-label="Black and white photo of an office tower against a cloudy sky" style="left:27px;top:3px;width:244px;height:286px;background:linear-gradient(160deg,#e6e6e6 0%,#9a9a9a 45%,#3a3a3a 100%)"></div>
  <div class="mark"></div>
  <p class="abs" style="left:297px;top:84px;font-size:11px;color:var(--blue)">About</p>
  <h2 class="abs" style="left:297px;top:100px;font-size:16px;line-height:1.1;font-weight:600;color:var(--ink)">Harbor Growth<br>Circle</h2>
  <p class="abs body" style="left:297px;top:172px;width:232px;font-size:6.8px">Lorem ipsum dolor sit amet, at laborum nibh duis mauris. Per ultrices lectus sed metus tristique eu. Diam suspendisse ac ipsum maecenas.</p>
  <p class="abs body" style="left:297px;top:203px;width:232px;font-size:6.8px">Eu adipiscing pulvinar eros. Mollis malesuada vel scelerisque, ligula quam non mauris neque eleifend etiam. Tincidunt duis velit lacus phasellus dui vitae, nec eu.</p>
  <div class="pg"></div>
</section>

<section class="slide c2 r6">
  <div class="abs" style="left:438px;top:0;width:121px;height:315px;background:var(--blue)"></div>
  <div class="abs" role="img" aria-label="Photo of a hand touching a glowing network of connected people icons" style="left:289px;top:71px;width:246px;height:195px;background:radial-gradient(circle at 55% 45%,#d98a4a 0%,#6a4a3a 30%,#1c2c4a 70%,#0d1830 100%);border:2px solid #fff"></div>
  <div class="mark on-blue"></div>
  <h2 class="abs" style="left:32px;top:96px;font-size:17px;font-weight:400;color:var(--ink)">How <b style="color:var(--blue);font-weight:600">We Do It.</b></h2>
  <ul class="bul abs body" style="left:32px;top:130px;width:230px;font-size:7px">
    <li>Lorem ipsum dolor sit amet, at laborum nibh duis mauris. Per ultrices lectus sed metus tristique eu. Diam suspendisse ac ipsum maecenas.</li>
    <li>Eu adipiscing pulvinar eros. Mollis malesuada vel scelerisque, ligula quam non mauris neque eleifend etiam. Tincidunt duis velit lacus phasellus dui vitae, nec eu.</li>
  </ul>
  <div class="pg on-blue"></div>
</section>

<!-- Row 7 -->
<section class="slide c1 r7">
  <div class="abs" role="img" aria-label="Photo of two business people shaking hands over a light hexagon pattern" style="left:0;top:0;width:279px;height:315px;background:linear-gradient(135deg,#dfe6ee 0%,#c3ccd8 45%,#7d8796 75%,#3b4452 100%)"></div>
  <div class="abs" style="left:279px;top:157px;width:280px;height:158px;background:var(--blue)"></div>
  <div class="mark"></div>
  <h2 class="abs" style="left:279px;top:52px;width:280px;text-align:center;font-size:21px;line-height:1.15;font-weight:400;color:var(--ink)"><b style="color:var(--blue);font-weight:500">Slide</b> Title<br>Goes Here!</h2>
  <div class="ico white" style="left:375px;top:143px"><svg viewBox="0 0 16 16"><rect x="2" y="5" width="12" height="8" rx="1" fill="#0b5cc0"/><rect x="6" y="3" width="4" height="3" fill="none" stroke="#0b5cc0" stroke-width="1.3"/></svg></div>
  <div class="ico white" style="left:488px;top:143px"><svg viewBox="0 0 16 16"><circle cx="8" cy="6.5" r="4.3" fill="#0b5cc0"/><rect x="6.3" y="11" width="3.4" height="3" fill="#0b5cc0"/></svg></div>
  <div class="abs" style="left:342px;top:182px;width:100px;text-align:center;color:#fff"><p style="font-size:10px;line-height:1.1">Title<br>Goes Here!</p><p style="font-size:5.6px;line-height:1.3;margin-top:5px">Lorem ipsum dolor sit amet, at laborum nibh duis mauris. Per ultrices lectus sed metus tristique eu.</p></div>
  <div class="abs" style="left:455px;top:182px;width:100px;text-align:center;color:#fff"><p style="font-size:10px;line-height:1.1">Title<br>Goes Here!</p><p style="font-size:5.6px;line-height:1.3;margin-top:5px">Lorem ipsum dolor sit amet, at laborum nibh duis mauris. Per ultrices lectus sed metus tristique eu.</p></div>
  <div class="pg on-blue"></div>
</section>

<section class="slide c2 r7">
  <h2 class="stitle"><b>Slide Title</b> <span style="font-weight:400;color:var(--ink)">Goes Here!</span></h2>
  <div class="mark"></div>
  <div class="abs" style="left:40px;top:112px;width:152px;text-align:right"><p class="item-t">Title Goes Here!</p><p class="tiny">Lorem ipsum dolor sit amet, at laborum nibh duis mauris. Per ultrices lectus sed metus tristique eu.</p></div>
  <div class="abs" style="left:40px;top:209px;width:152px;text-align:right"><p class="item-t">Title Goes Here!</p><p class="tiny">Lorem ipsum dolor sit amet, at laborum nibh duis mauris. Per ultrices lectus sed metus tristique eu.</p></div>
  <div class="abs" style="left:371px;top:112px;width:152px"><p class="item-t">Title Goes Here!</p><p class="tiny">Lorem ipsum dolor sit amet, at laborum nibh duis mauris. Per ultrices lectus sed metus tristique eu.</p></div>
  <div class="abs" style="left:371px;top:209px;width:152px"><p class="item-t">Title Goes Here!</p><p class="tiny">Lorem ipsum dolor sit amet, at laborum nibh duis mauris. Per ultrices lectus sed metus tristique eu.</p></div>
  <div class="ico" style="left:219px;top:115px"><svg viewBox="0 0 16 16"><circle cx="8" cy="6.5" r="4.3" fill="#fff"/><rect x="6.3" y="11" width="3.4" height="3" fill="#fff"/></svg></div>
  <div class="ico" style="left:335px;top:115px"><svg viewBox="0 0 16 16"><circle cx="7" cy="7" r="4" fill="none" stroke="#fff" stroke-width="1.8"/><line x1="10" y1="10" x2="14" y2="14" stroke="#fff" stroke-width="2"/></svg></div>
  <div class="ico" style="left:219px;top:212px"><svg viewBox="0 0 16 16"><rect x="3" y="2" width="10" height="12" rx="1" fill="none" stroke="#fff" stroke-width="1.5"/><line x1="5.5" y1="6" x2="10.5" y2="6" stroke="#fff"/><line x1="5.5" y1="8.5" x2="10.5" y2="8.5" stroke="#fff"/><line x1="5.5" y1="11" x2="10.5" y2="11" stroke="#fff"/></svg></div>
  <div class="ico" style="left:335px;top:212px"><svg viewBox="0 0 16 16"><line x1="3" y1="3" x2="13" y2="13" stroke="#fff" stroke-width="2"/><line x1="13" y1="3" x2="3" y2="13" stroke="#fff" stroke-width="2"/></svg></div>
  <div class="pg"></div>
</section>

<!-- Row 8 -->
<section class="slide c1 r8">
  <svg class="decor" viewBox="0 0 559 315" aria-hidden="true">
    <polygon points="559,0 559,315 300,315" fill="#0a3a8a"/>
    <polygon points="559,40 559,315 345,315" fill="#0b5cc0"/>
  </svg>
  <h2 class="abs" style="left:45px;top:160px;font-size:28px;font-weight:600;color:var(--navy)">Section Braek</h2>
  <p class="abs body" style="left:45px;top:197px;width:235px;font-size:7.5px">Lorem ipsum dolor sit amet, at laborum nibh duis mauris. Per ultrices lectus sed metus tristique eu.</p>
</section>

<section class="slide c2 r8">
  <h2 class="stitle"><b>Slide Title</b> <span style="font-weight:400;color:var(--ink)">Goes Here!</span></h2>
  <div class="mark"></div>
  <table class="ptable">
    <thead><tr><th>Partner Type</th><th>What they do</th><th>How they earn money</th><th>When you use it</th></tr></thead>
    <tbody>
      <tr><td>Referral</td><td>Introduce prospective customers to you</td><td>You pay them a commission when you close the deal</td><td>To incentivize any partner to bring you leads</td></tr>
      <tr><td>Procurement Reseller</td><td>Purchase software on behalf of your end customer</td><td>Charge fees to your end customer</td><td>When required by your customer</td></tr>
      <tr><td>Value added Reseller (VAR)</td><td>Resell your software &amp; services, may combine with their own services and other products</td><td>Margin on resales, value added services around your product</td><td>Increase your reach to partners' customer base and/or other geos</td></tr>
      <tr><td>Distributor</td><td>Recruits and manages a large number of resellers for you</td><td>Margin on resales through VARs</td><td>Scale sales of low touch products</td></tr>
      <tr><td>Global Systems Integrator (GSI)</td><td>IT services &amp; solutions involving many products &amp; services</td><td>Consulting services</td><td>Your product aids delivery of services</td></tr>
      <tr><td>OEM</td><td>License your products to be bundled with their products</td><td>Selling their product that includes yours</td><td>Your product adds value to another vendor's product</td></tr>
    </tbody>
  </table>
  <div class="pg"></div>
</section>

<!-- Row 9 -->
<section class="slide c1 r9">
  <h2 class="stitle plain" style="font-size:18px">Partner <b>Complexity</b> and <b>Value Spectrum</b></h2>
  <div class="mark"></div>
  <svg class="decor" viewBox="0 0 559 315" aria-hidden="true">
    <line x1="66" y1="155" x2="494" y2="155" stroke="#c9ced6" stroke-width="3"/>
    <polygon points="58,155 70,149 70,161" fill="#c9ced6"/>
    <polygon points="502,155 490,149 490,161" fill="#c9ced6"/>
    <g fill="#fff" stroke="#0b5cc0" stroke-width="2">
      <circle cx="102" cy="155" r="5"/><circle cx="144" cy="155" r="5"/><circle cx="279" cy="155" r="5"/><circle cx="433" cy="155" r="5"/><circle cx="457" cy="155" r="5"/>
    </g>
    <g stroke="#0b5cc0" stroke-dasharray="2 2">
      <line x1="102" y1="160" x2="102" y2="216"/><line x1="144" y1="160" x2="144" y2="240"/><line x1="279" y1="160" x2="279" y2="216"/><line x1="433" y1="160" x2="433" y2="240"/><line x1="457" y1="160" x2="457" y2="216"/>
    </g>
    <rect x="232" y="92" width="94" height="42" rx="21" fill="#0a3a8a"/>
  </svg>
  <p class="abs tiny" style="left:63px;top:102px;width:100px;text-align:center;color:var(--ink);font-size:6.5px">Low Complexity<br>Quick &amp; Easy<br>Lower Value</p>
  <p class="abs tiny" style="left:418px;top:102px;width:100px;text-align:center;color:var(--ink);font-size:6.5px">High Complexity<br>Longer time to<br>establish Higher<br>Value</p>
  <p class="abs tiny" style="left:62px;top:219px;width:80px;text-align:center;color:var(--ink);font-size:6.5px">Procurement</p>
  <p class="abs tiny" style="left:104px;top:243px;width:80px;text-align:center;color:var(--ink);font-size:6.5px">Referral</p>
  <p class="abs tiny" style="left:234px;top:219px;width:90px;text-align:center;color:var(--ink);font-size:6.5px">Value Added<br>Reseller (VAR)</p>
  <p class="abs tiny" style="left:417px;top:219px;width:80px;text-align:center;color:var(--ink);font-size:6.5px">OEM</p>
  <p class="abs tiny" style="left:388px;top:243px;width:90px;text-align:center;color:var(--ink);font-size:6.5px">Global Systems<br>Integrator (GSI)</p>
  <div class="pg"></div>
</section>

<section class="slide c2 r9">
  <h2 class="stitle"><b>Slide Title</b> <span style="font-weight:400;color:var(--ink)">Goes Here!</span></h2>
  <div class="mark"></div>
  <div class="abs" role="img" aria-label="Photo of a laptop and printed charts on a desk" style="left:45px;top:97px;width:226px;height:110px;background:linear-gradient(135deg,#f2f4f7 0%,#c9d3df 50%,#6f8aa8 100%)"></div>
  <div class="abs" role="img" aria-label="Photo of hands joining two puzzle pieces" style="left:287px;top:97px;width:226px;height:110px;background:linear-gradient(135deg,#d8b58a 0%,#9a7654 45%,#3d4a5c 100%)"></div>
  <p class="abs body" style="left:45px;top:215px;width:226px;text-align:center">Lorem ipsum dolor sit amet, at laborum nibh duis mauris. Per ultrices lectus sed metus tristique eu. Diam suspendisse ac ipsum.</p>
  <p class="abs body" style="left:287px;top:215px;width:226px;text-align:center">Lorem ipsum dolor sit amet, at laborum nibh duis mauris. Per ultrices lectus sed metus tristique eu. Diam suspendisse ac ipsum.</p>
  <div class="pg"></div>
</section>

<!-- Row 10 -->
<section class="slide c1 r10">
  <svg class="decor" viewBox="0 0 559 315" aria-hidden="true">
    <rect x="420" y="0" width="139" height="315" fill="#0b5cc0"/>
    <polygon points="559,120 559,315 460,315" fill="#0a3a8a"/>
  </svg>
  <h2 class="stitle"><b>Slide Title</b> <span style="font-weight:400;color:var(--ink)">Goes Here!</span></h2>
  <div class="mark on-blue"></div>
  <div class="abs" style="left:36px;top:95px;width:180px"><p class="item-t" style="font-size:9px;margin-bottom:4px">Title Goes Here!</p>
    <ul class="bul tiny"><li>Lorem ipsum dolor sit amet</li><li>Per ultrices lectus sed metus tristique.</li><li>Diam suspendisse ac ipsum.</li><li>Aliquet imperdiet et lobortis.</li><li>Per ultrices lectus sed metus tristique.</li></ul></div>
  <div class="abs" style="left:228px;top:95px;width:180px"><p class="item-t" style="font-size:9px;margin-bottom:4px">Title Goes Here!</p>
    <ul class="bul tiny"><li>Lorem ipsum dolor sit amet</li><li>Per ultrices lectus sed metus tristique.</li><li>Diam suspendisse ac ipsum.</li><li>Aliquet imperdiet et lobortis.</li><li>Per ultrices lectus sed metus tristique.</li></ul></div>
  <div class="abs" style="left:36px;top:197px;width:180px"><p class="item-t" style="font-size:9px;margin-bottom:4px">Title Goes Here!</p>
    <ul class="bul tiny"><li>Lorem ipsum dolor sit amet</li><li>Per ultrices lectus sed metus tristique.</li><li>Diam suspendisse ac ipsum.</li><li>Aliquet imperdiet et lobortis.</li><li>Per ultrices lectus sed metus tristique.</li></ul></div>
  <div class="abs" style="left:228px;top:197px;width:180px"><p class="item-t" style="font-size:9px;margin-bottom:4px">Title Goes Here!</p>
    <ul class="bul tiny"><li>Lorem ipsum dolor sit amet</li><li>Per ultrices lectus sed metus tristique.</li><li>Diam suspendisse ac ipsum.</li><li>Aliquet imperdiet et lobortis.</li><li>Per ultrices lectus sed metus tristique.</li></ul></div>
  <div class="pg on-blue"></div>
</section>

<section class="slide c2 r10">
  <div class="abs" role="img" aria-label="Faint puzzle piece image on a blue panel" style="left:189px;top:0;width:181px;height:315px;background:linear-gradient(180deg,#2a82dc 0%,#1f73cf 50%,#2a82dc 100%)"></div>
  <div class="mark"></div>
  <h2 class="abs" style="left:189px;top:125px;width:181px;text-align:center;font-size:20px;line-height:1.15;font-weight:400;color:#fff">Slide Title<br>Goes Here!</h2>
  <div class="ico" style="left:175px;top:67px;background:var(--navy)"><svg viewBox="0 0 16 16"><circle cx="8" cy="6.5" r="4.3" fill="#fff"/><rect x="6.3" y="11" width="3.4" height="3" fill="#fff"/></svg></div>
  <div class="ico" style="left:357px;top:67px;background:var(--navy)"><svg viewBox="0 0 16 16"><rect x="2" y="3" width="12" height="8" rx="1" fill="none" stroke="#fff" stroke-width="1.5"/><rect x="6" y="12" width="4" height="2" fill="#fff"/></svg></div>
  <div class="ico" style="left:175px;top:180px;background:var(--navy)"><svg viewBox="0 0 16 16"><line x1="3" y1="3" x2="13" y2="13" stroke="#fff" stroke-width="2"/><line x1="13" y1="3" x2="3" y2="13" stroke="#fff" stroke-width="2"/></svg></div>
  <div class="ico" style="left:357px;top:180px;background:var(--navy)"><svg viewBox="0 0 16 16"><rect x="3" y="9" width="2.5" height="5" fill="#fff"/><rect x="7" y="6" width="2.5" height="8" fill="#fff"/><rect x="11" y="3" width="2.5" height="11" fill="#fff"/></svg></div>
  <div class="abs" style="left:35px;top:56px;width:122px;text-align:right"><p class="item-t" style="font-size:9px;color:var(--navy)">Title<br>Goes Here!</p><p class="tiny">Lorem ipsum dolor sit amet, at laborum nibh duis mauris. Per ultrices lectus sed metus tristique eu. Lorem ipsum dolor sit amet, at laborum nibh duis mauris.</p></div>
  <div class="abs" style="left:35px;top:170px;width:122px;text-align:right"><p class="item-t" style="font-size:9px;color:var(--navy)">Title<br>Goes Here!</p><p class="tiny">Lorem ipsum dolor sit amet, at laborum nibh duis mauris. Per ultrices lectus sed metus tristique eu. Lorem ipsum dolor sit amet, at laborum nibh duis mauris.</p></div>
  <div class="abs" style="left:405px;top:56px;width:122px"><p class="item-t" style="font-size:9px;color:var(--navy)">Title<br>Goes Here!</p><p class="tiny">Lorem ipsum dolor sit amet, at laborum nibh duis mauris. Per ultrices lectus sed metus tristique eu. Lorem ipsum dolor sit amet, at laborum nibh duis mauris.</p></div>
  <div class="abs" style="left:405px;top:170px;width:122px"><p class="item-t" style="font-size:9px;color:var(--navy)">Title<br>Goes Here!</p><p class="tiny">Lorem ipsum dolor sit amet, at laborum nibh duis mauris. Per ultrices lectus sed metus tristique eu. Lorem ipsum dolor sit amet, at laborum nibh duis mauris.</p></div>
  <div class="pg"></div>
</section>

<!-- Row 11 -->
<section class="slide c1 r11">
  <h2 class="stitle"><b>Slide Title</b> <span style="font-weight:400;color:var(--ink)">Goes Here!</span></h2>
  <div class="mark"></div>
  <svg class="decor" viewBox="0 0 559 315" aria-hidden="true">
    <line x1="0" y1="129" x2="533" y2="129" stroke="#b7bec9" stroke-dasharray="2 2"/>
    <g fill="#fff" stroke="#0a3a8a" stroke-width="2.5">
      <circle cx="111" cy="129" r="19"/><circle cx="223" cy="129" r="19"/><circle cx="336" cy="129" r="19"/><circle cx="447" cy="129" r="19"/>
    </g>
    <g font-family="Rubik, Arial, sans-serif" font-size="17" fill="#0b5cc0" text-anchor="middle">
      <text x="111" y="135">1</text><text x="223" y="135">2</text><text x="336" y="135">3</text><text x="447" y="135">4</text>
    </g>
  </svg>
  <div class="abs" style="left:66px;top:172px;width:90px;text-align:center"><p class="item-t">Title<br>Goes Here!</p><p class="tiny" style="margin-top:4px">Lorem ipsum dolor sit amet, at laborum nibh duis mauris. Per ultrices lectus sed metus tristique eu.</p></div>
  <div class="abs" style="left:178px;top:172px;width:90px;text-align:center"><p class="item-t">Title<br>Goes Here!</p><p class="tiny" style="margin-top:4px">Lorem ipsum dolor sit amet, at laborum nibh duis mauris. Per ultrices lectus sed metus tristique eu.</p></div>
  <div class="abs" style="left:291px;top:172px;width:90px;text-align:center"><p class="item-t">Title<br>Goes Here!</p><p class="tiny" style="margin-top:4px">Lorem ipsum dolor sit amet, at laborum nibh duis mauris. Per ultrices lectus sed metus tristique eu.</p></div>
  <div class="abs" style="left:402px;top:172px;width:90px;text-align:center"><p class="item-t">Title<br>Goes Here!</p><p class="tiny" style="margin-top:4px">Lorem ipsum dolor sit amet, at laborum nibh duis mauris. Per ultrices lectus sed metus tristique eu.</p></div>
  <div class="pg"></div>
</section>

<section class="slide c2 r11">
  <h2 class="stitle"><b>Slide Title</b> <span style="font-weight:400;color:var(--ink)">Goes Here!</span></h2>
  <div class="mark"></div>
  <svg class="abs" style="left:28px;top:78px" width="250" height="200" viewBox="0 0 250 200" aria-label="Bar chart of three series across categories A to F" role="img">
    <g font-family="Rubik, Arial, sans-serif" font-size="6" fill="#4b525c" text-anchor="end">
      <text x="12" y="182">0</text><text x="12" y="155">1</text><text x="12" y="128">2</text><text x="12" y="101">3</text><text x="12" y="74">4</text><text x="12" y="47">5</text><text x="12" y="20">6</text>
    </g>
    <g stroke="#e1e4ea"><line x1="18" y1="153" x2="240" y2="153"/><line x1="18" y1="126" x2="240" y2="126"/><line x1="18" y1="99" x2="240" y2="99"/><line x1="18" y1="72" x2="240" y2="72"/><line x1="18" y1="45" x2="240" y2="45"/><line x1="18" y1="18" x2="240" y2="18"/></g>
    <line x1="18" y1="180" x2="240" y2="180" stroke="#9aa1ab"/>
    <g fill="#0a3a8a"><rect x="26" y="64" width="7" height="116"/><rect x="62" y="113" width="7" height="67"/><rect x="98" y="86" width="7" height="94"/><rect x="134" y="59" width="7" height="121"/><rect x="170" y="64" width="7" height="116"/><rect x="206" y="113" width="7" height="67"/></g>
    <g fill="#1a75d1"><rect x="34" y="115" width="7" height="65"/><rect x="70" y="61" width="7" height="119"/><rect x="106" y="131" width="7" height="49"/><rect x="142" y="104" width="7" height="76"/><rect x="178" y="115" width="7" height="65"/><rect x="214" y="61" width="7" height="119"/></g>
    <g fill="#24262b"><rect x="42" y="126" width="7" height="54"/><rect x="78" y="126" width="7" height="54"/><rect x="114" y="99" width="7" height="81"/><rect x="150" y="45" width="7" height="135"/><rect x="186" y="126" width="7" height="54"/><rect x="222" y="126" width="7" height="54"/></g>
    <g font-family="Rubik, Arial, sans-serif" font-size="6" fill="#4b525c" text-anchor="middle">
      <text x="37" y="191">A</text><text x="73" y="191">B</text><text x="109" y="191">C</text><text x="145" y="191">D</text><text x="181" y="191">E</text><text x="217" y="191">F</text>
    </g>
  </svg>
  <p class="abs body" style="left:287px;top:81px;width:240px;font-size:6.8px">Lorem ipsum dolor sit amet, at laborum nibh duis mauris. Per ultrices lectus sed metus tristique eu. Diam suspendisse ac ipsum maecenas.</p>
  <table class="dtable">
    <thead><tr><th style="width:40%">Category</th><th>Series 1</th><th>Series 2</th><th>Series 3</th></tr></thead>
    <tbody>
      <tr><td>Text Goes Here</td><td>4.3</td><td>2.4</td><td>2</td></tr>
      <tr><td>Text Goes Here</td><td>2.5</td><td>4.4</td><td>2</td></tr>
      <tr><td>Text Goes Here</td><td>3.5</td><td>1.8</td><td>3</td></tr>
      <tr><td>Text Goes Here</td><td>4.5</td><td>2.8</td><td>5</td></tr>
      <tr><td>Text Goes Here</td><td>4.3</td><td>2.4</td><td>2</td></tr>
      <tr><td>Text Goes Here</td><td>2.5</td><td>4.4</td><td>2</td></tr>
    </tbody>
  </table>
  <div class="pg"></div>
</section>

<!-- Closing -->
<section class="slide cc r12">
  <div class="fill" role="img" aria-label="Photo looking up at a glass office tower, tinted blue" style="background:linear-gradient(110deg,#0b4aa6 0%,#1b5fb4 45%,#5a86bf 75%,#9fb7d6 100%)"></div>
  <svg class="decor" viewBox="0 0 559 315" aria-hidden="true">
    <polygon points="559,150 559,315 410,315" fill="#fff"/>
    <circle cx="548" cy="305" r="82" fill="#0b5cc0"/>
  </svg>
  <div class="brand" style="top:120px;color:#fff"><i></i><span>Harbor Growth Circle</span></div>
  <h2 class="abs" style="left:47px;top:196px;font-size:12px;font-weight:500;color:#fff">Contact Us</h2>
  <p class="contact-line" style="top:228px"><svg viewBox="0 0 10 10"><path d="M2 1 L4 1 L4.8 3.2 L3.6 4 Q4.6 6 6 6.5 L6.8 5.3 L9 6 L9 8 Q5 9 2 5 Q1 3 2 1Z" fill="#fff"/></svg>555-0142-7788</p>
  <p class="contact-line" style="top:243px"><svg viewBox="0 0 10 10"><circle cx="5" cy="5" r="4" fill="none" stroke="#fff" stroke-width="1.2"/><circle cx="5" cy="5" r="1.5" fill="#fff"/></svg>info@harborgrowthcircle.com</p>
  <p class="contact-line" style="top:258px"><svg viewBox="0 0 10 10"><circle cx="5" cy="5" r="4" fill="none" stroke="#fff" stroke-width="1"/><line x1="1" y1="5" x2="9" y2="5" stroke="#fff" stroke-width=".8"/><ellipse cx="5" cy="5" rx="1.8" ry="4" fill="none" stroke="#fff" stroke-width=".8"/></svg>www.harborgrowthcircle.com</p>
</section>

</body>
</html>
```